Business cards

I would like a black background with the design I previously chose. I need 2 sets of cards. Mine will have Marisol Brandt, Broker/Owner, 307-555-0148 and marisol.harborpeak@mailvista.com
The second set will read, Dana Rutledge, Realtor 307-555-0172, dana.harborpeak@mailvista.com

Industry/Entity Type

Business

```html
<!DOCTYPE html>
<html lang="en">
<head>
<meta charset="utf-8">
<title>Harbor Peak Business Cards</title>
<link href="https://fonts.googleapis.com/css2?family=Tinos:wght@400;700&family=Roboto:wght@400&display=swap" rel="stylesheet">
<style>
  :root {
    --backdrop: #161616;
    --card: #222325;
    --silver: #c4c4c4;
    --silver-bright: #e2e2e2;
    --ink: #f2f2f2;
    --icon: #d8d8d8;
  }
  * { margin: 0; padding: 0; box-sizing: border-box; }
  html, body { width: 1200px; height: 960px; overflow: hidden; }
  body {
    background: var(--backdrop);
    position: relative;
    font-family: "Tinos", "Times New Roman", serif;
  }
  .card {
    position: absolute;
    background: var(--card);
    box-shadow: 0 4px 14px rgba(0,0,0,0.6);
  }
  .card--front { left: 313px; top: 113px; width: 600px; height: 342px; }
  .card--back  { left: 311px; top: 473px; width: 600px; height: 340px; }

  .brand {
    position: absolute;
    left: 0; right: 0;
    display: flex;
    align-items: center;
    justify-content: center;
    gap: 12px;
    color: var(--silver);
    font-family: "Tinos", "Times New Roman", serif;
    font-weight: 700;
    letter-spacing: 0.04em;
  }
  .brand__dot {
    border: 2px solid var(--silver);
    border-radius: 50%;
  }
  .card--front .brand { top: 132px; font-size: 26px; }
  .card--front .brand__dot { width: 22px; height: 22px; }
  .card--back .brand { top: 140px; font-size: 36px; }
  .card--back .brand__dot { width: 32px; height: 32px; }

  .holder {
    position: absolute;
    left: 0; right: 0; top: 207px;
    text-align: center;
  }
  .holder__name {
    font-size: 22px;
    font-weight: 700;
    color: var(--silver);
    letter-spacing: 0.01em;
    line-height: 26px;
  }
  .holder__title {
    font-size: 16px;
    color: var(--ink);
    letter-spacing: 0.04em;
    line-height: 20px;
  }
  .contact {
    position: absolute;
    left: 0; right: 0;
    display: flex;
    justify-content: center;
    align-items: center;
    gap: 4px;
    font-size: 14.5px;
    color: var(--ink);
  }
  .contact--primary { top: 258px; }
  .contact--web { top: 278px; }
  .contact__item { display: flex; align-items: center; gap: 4px; }
  .contact svg { fill: var(--icon); }

  .back-url {
    position: absolute;
    left: 0; right: 0; top: 286px;
    text-align: center;
    font-family: "Roboto", "Arial", sans-serif;
    font-size: 15px;
    letter-spacing: 0.26em;
    color: var(--ink);
  }
</style>
</head>
<body>
  <section class="card card--front">
    <div class="brand">
      <span class="brand__dot"></span>
      <span class="brand__name">HARBOR PEAK</span>
    </div>
    <div class="holder">
      <div class="holder__name">MARISOL BRANDT</div>
      <div class="holder__title">BROKER/OWNER</div>
    </div>
    <div class="contact contact--primary">
      <span class="contact__item">
        <svg width="9" height="14" viewBox="0 0 9 14" aria-hidden="true"><path d="M1.5 0h6A1.5 1.5 0 0 1 9 1.5v11A1.5 1.5 0 0 1 7.5 14h-6A1.5 1.5 0 0 1 0 12.5v-11A1.5 1.5 0 0 1 1.5 0zM1.3 1.6v9.6h6.4V1.6zM4.5 11.8a.8.8 0 1 0 0 1.6.8.8 0 0 0 0-1.6z"/></svg>
        307-555-0148
      </span>
      <span class="contact__item">
        <svg width="12" height="9" viewBox="0 0 12 9" aria-hidden="true"><path d="M0 0h12v1L6 5 0 1zM0 2.3l6 4 6-4V9H0z"/></svg>
        marisol.harborpeak@mailvista.com
      </span>
    </div>
    <div class="contact contact--web">
      <span class="contact__item">
        <svg width="12" height="12" viewBox="0 0 12 12" aria-hidden="true"><circle cx="6" cy="6" r="6"/><path d="M3 3.5c1 .3 1.5 1.2 1 2-.4.7.3 1.6 1.2 1.4.8-.2 1 .9.4 1.7M8.2 2.2c-.6.8-.1 1.7.8 1.8" stroke="#222325" stroke-width="1.1" fill="none"/></svg>
        www.harborpeak.com
      </span>
    </div>
  </section>

  <section class="card card--back">
    <div class="brand">
      <span class="brand__dot"></span>
      <span class="brand__name">HARBOR PEAK</span>
    </div>
    <div class="back-url">www.harborpeak.com</div>
  </section>
</body>
</html>
```